Amazing Homepage required for Ireland's Top Crowdfunding site

Design/ PSD Files required.

BrightHarbour.com is the market leader in crowd lending/peer to peer lending in Ireland. Businesses/SME’s can borrow anything from €5,000 to €100,000 at interest rates much more favourable than those offered by the banks. BH is also a quicker and less bureaucratic than traditional lending institutions. We are a viable alternative to banks and traditional sources of finance.

Our lenders are members of the public and they can lend directly to Irish businesses in amounts from €50 to €2,000. They get a better rate of return than deposit accounts, as well as the feel good factor of supporting a local business.

We have just completed a full rebrand of our logo and colours and would now like to utilise these to best effect by implementing them in a total redesign of our homepage to attract borrowers and lenders. Please see the attached files for the brand guidelines and logo/colours to be used.

We are looking for a designer to utilise our new branding in a creative way, conveying that we are modern, trustworthy, competitive and friendly/local.

We currently have two different user groups:
1- Lenders; this currently consists of members of the public but in future will expand to include financial institutions

2- Business borrowers looking for funds for their business

Embracing and balancing both of these user groups is difficult so we would like the homepage to primarily target borrowers but incorporate clear alternative calls to action for lenders/prospective lenders as well.

We would like:
Infinite scroll homepage
New logo and tagline on a fixed header which should also include; ‘Marketplace’ ‘About’ ‘FAQ’ and a clear login button
A static full bleed image
Overlaid over this we would like a loan calculator in a similar style/functionality to this one on www.quellmoor.com. It should have:
an image of a slider icon with amounts from €0 to €100,000
A text field with ‘Business Loan amount’ which fills when the slider is moved
Then, a text field called ‘Monthly repayment’
An email field with a clear call to action ie ‘Go’ or ‘Get Started’
The purpose of this is to enable prospective borrowers to quickly and easily get a quote estimate for their loan
Underneath this we would like to have an alternate call to action to target prospective lenders; something like ‘Looking to Lend?’

Further down the page we would like to have a heading ‘What is Bright Harbour?’
(include information from company overview)

3 images to illustrate loans live in our Marketplace

Target Market(s)

This Homepge should appeal to small business owners

Industry/Entity Type

Crowd

Number of Pages Required

1 page

Font styles to use
Sans Serif

Requirements
Must have
• Linear clean and modern homepage
• Clear calls to action
Nice to have
• Ideas for how video/rich media might be incorporated into a future iteration of the homepage

```html
<!DOCTYPE html>
<html lang="en">
<head>
<meta charset="utf-8">
<title>Bright Harbour – Business Lending</title>
<link href="https://fonts.googleapis.com/css2?family=Arimo:wght@400;700&display=swap" rel="stylesheet">
<style>
:root{
  --brand:#cf6b3e;
  --brand-dark:#b9572c;
  --ink:#333333;
  --muted:#8a8a8a;
  --line:#d4d4d4;
  --bg:#ffffff;
  --night:#121212;
  --hero-a:#0c1f8c;
  --hero-b:#3c6cf2;
  --band-a:#1e3340;
  --band-b:#44606a;
}
*{box-sizing:border-box;margin:0;padding:0}
html,body{width:1200px;height:2804px;overflow:hidden;background:var(--bg)}
body{font-family:"Arimo",Arial,sans-serif;color:var(--ink);position:relative}
.abs{position:absolute}

/* header */
.site-header{position:absolute;left:0;top:0;width:1200px;height:140px;background:#fff}
.brand{position:absolute;left:99px;top:62px;display:flex;align-items:center;gap:10px}
.brand-mark{width:22px;height:22px;background:var(--brand)}
.brand-name{font-size:24px;color:var(--ink)}
.brand-tagline{position:absolute;left:99px;top:96px;font-size:12px;color:var(--brand)}
.contact-line{position:absolute;right:99px;top:31px;font-size:12px;letter-spacing:.3px}
.contact-line .k{color:var(--brand)}
.contact-line .gap{display:inline-block;width:24px}
.main-nav{position:absolute;left:652px;top:94px;display:flex;gap:0;font-size:12px;letter-spacing:.4px}
.main-nav a{color:var(--ink);text-decoration:none;margin-right:56px}
.btn-login{position:absolute;left:1002px;top:86px;width:99px;height:26px;background:var(--brand);color:#111;font-size:11px;font-weight:700;display:flex;align-items:center;justify-content:center;letter-spacing:.5px}

/* hero */
.hero{position:absolute;left:0;top:140px;width:1200px;height:466px;background:radial-gradient(circle at 35% 40%,#5b8cff 0%,var(--hero-b) 35%,var(--hero-a) 100%)}
.hero-band{position:absolute;left:99px;top:180px;width:1002px;height:102px;background:rgba(225,230,245,.72);display:flex;align-items:center;justify-content:center;font-size:41px;font-weight:700;letter-spacing:3px;word-spacing:10px;color:#111}
.hero-arrow{position:absolute;top:212px;width:36px;height:36px}

/* section titles */
.section-title{position:absolute;left:0;width:1200px;text-align:center;font-size:24px;font-weight:700;color:var(--brand)}
.title-rule{position:absolute;left:525px;width:150px;height:1px;background:var(--line)}

/* calculator */
.calc-label{position:absolute;left:99px;font-size:16px;font-weight:700;letter-spacing:.3px}
.range-end{position:absolute;font-size:17px;font-weight:700;color:var(--brand)}
.range-value{position:absolute;font-size:12px;color:var(--muted)}
.step-btn{position:absolute;width:28px;height:28px}
.track{position:absolute;left:158px;width:882px;height:9px;background:var(--line)}
.track-fill{position:absolute;left:0;top:0;height:9px;background:var(--brand)}
.handle{position:absolute;width:44px;height:44px;border-radius:50%;background:#fff;box-shadow:0 2px 6px rgba(0,0,0,.25);display:flex;align-items:center;justify-content:center}
.sum{position:absolute;top:1074px;font-size:17px;font-weight:700}
.sum-op{position:absolute;top:1064px;font-size:32px;font-weight:700;color:var(--brand)}
.rep-title{position:absolute;top:1162px;font-size:16px;font-weight:700;letter-spacing:.3px}
.rep-line{position:absolute;left:99px;font-size:12px;font-weight:700;letter-spacing:.3px}
.rep-line b{color:var(--brand);font-size:15px}
.email-field{position:absolute;left:675px;top:1222px;width:213px;height:36px;border:1px solid #c8c8c8;font-size:13px;color:#999;padding:0 14px;display:flex;align-items:center}
.btn-start{position:absolute;left:901px;top:1222px;width:200px;height:36px;background:linear-gradient(#e08459,var(--brand-dark));color:#222;font-size:13px;font-weight:700;display:flex;align-items:center;justify-content:center;letter-spacing:.4px}

/* about band */
.about{position:absolute;left:0;top:1316px;width:1200px;height:474px;background:linear-gradient(120deg,var(--band-a),var(--band-b) 50%,var(--band-a))}
.about-title{position:absolute;left:0;top:146px;width:1200px;text-align:center;font-size:24px;font-weight:700;color:var(--brand)}
.about-copy{position:absolute;left:370px;top:214px;width:460px;text-align:center;font-size:12px;line-height:21px;color:#fff}
.btn-read{position:absolute;left:548px;top:291px;width:110px;height:36px;background:var(--brand);color:#222;font-size:12px;font-weight:700;display:flex;align-items:center;justify-content:center}

/* loan cards */
.loan-card{position:absolute;top:1934px;width:321px;height:421px;border:1px solid #e2e2e2;background:#fff}
.loan-photo{height:190px}
.loan-title{position:absolute;left:20px;top:208px;font-size:15px;font-weight:700}
.loan-text{position:absolute;left:20px;top:234px;width:282px;font-size:11px;line-height:18px;color:#666}
.loan-amount{position:absolute;left:20px;top:347px;font-size:13px;font-weight:700;color:#444}
.loan-amount span{font-weight:400;color:var(--muted);font-size:11px}
.loan-bar{position:absolute;left:20px;top:369px;width:281px;height:12px;background:#b5b5b5}
.loan-bar i{display:block;height:12px;background:var(--brand)}
.loan-pct{position:absolute;left:20px;top:392px;font-size:13px;font-weight:700;color:#444}
.loan-days{position:absolute;right:20px;top:394px;font-size:11px;color:#555}

/* footer */
.site-footer{position:absolute;left:0;top:2435px;width:1200px;height:303px;background:var(--brand);color:#fff}
.foot-sep{position:absolute;top:0;width:10px;height:303px;background:linear-gradient(90deg,rgba(0,0,0,.08),rgba(0,0,0,0))}
.foot-col{position:absolute;top:32px}
.foot-col h4{font-size:13px;font-weight:400;letter-spacing:.4px;margin-bottom:22px}
.foot-col li{list-style:none;font-size:11px;line-height:21px}
.contact-row{display:flex;gap:14px;font-size:11px;line-height:21px;margin-bottom:12px}
.contact-row svg{flex:none;margin-top:3px}
.social{display:flex;gap:4px;margin-top:10px}
.social i{display:block;width:17px;height:17px;background:#fff}
.legal{position:absolute;left:0;top:2738px;width:1200px;height:66px;background:var(--night);color:#888;font-size:11px;display:flex;align-items:center;justify-content:center}
</style>
</head>
<body>

<header class="site-header">
  <div class="brand"><span class="brand-mark"></span><span class="brand-name">Bright Harbour</span></div>
  <div class="brand-tagline">the business lending people</div>
  <div class="contact-line"><span class="k">E MAIL</span> : HELLO@BRIGHTHARBOUR.IE<span class="gap"></span><span class="k">PHONE</span> : 1800 - 555 - 010</div>
  <nav class="main-nav"><a href="#">MARKETPLACE</a><a href="#">ABOUT</a><a href="#">FAQ</a></nav>
  <div class="btn-login">LOGIN</div>
</header>

<section class="hero" role="img" aria-label="Businessman in a suit touching a glowing blue digital interface">
  <svg class="hero-arrow" style="left:28px" viewBox="0 0 36 36"><circle cx="18" cy="18" r="16" fill="none" stroke="rgba(255,255,255,.5)" stroke-width="2"/><path d="M21 11l-7 7 7 7" fill="none" stroke="rgba(255,255,255,.6)" stroke-width="2"/></svg>
  <svg class="hero-arrow" style="right:28px" viewBox="0 0 36 36"><circle cx="18" cy="18" r="16" fill="none" stroke="rgba(255,255,255,.5)" stroke-width="2"/><path d="M15 11l7 7-7 7" fill="none" stroke="rgba(255,255,255,.6)" stroke-width="2"/></svg>
  <div class="hero-band">ALWAYS BE THE BEST MARKET</div>
</section>

<h2 class="section-title" style="top:642px">MARKET PLACE</h2>
<div class="title-rule" style="top:679px"></div>

<!-- loan amount -->
<div class="calc-label" style="top:731px">BUSINESS LOAN AMOUNT</div>
<div class="range-end" style="left:99px;top:781px">€ 0</div>
<div class="range-end" style="right:99px;top:781px">€ 100,000</div>
<div class="range-value" style="left:636px;top:784px">€ 6577</div>
<svg class="step-btn" style="left:99px;top:811px" viewBox="0 0 28 28"><circle cx="14" cy="14" r="13" fill="none" stroke="#555"/><path d="M9 14h10M14 9v10" stroke="#555"/></svg>
<div class="track" style="top:821px"><div class="track-fill" style="width:500px"></div></div>
<div class="handle" style="left:636px;top:803px"><svg width="20" height="12" viewBox="0 0 20 12"><path d="M7 1L2 6l5 5M13 1l5 5-5 5" fill="none" stroke="var(--brand)" stroke-width="1.6"/></svg></div>
<svg class="step-btn" style="left:1073px;top:811px" viewBox="0 0 28 28"><circle cx="14" cy="14" r="13" fill="none" stroke="#555"/><path d="M9 14h10" stroke="#555"/></svg>

<!-- monthly repayment -->
<div class="calc-label" style="top:911px">MONTHLY REPAYMENT</div>
<div class="range-end" style="left:99px;top:963px">€ 0</div>
<div class="range-end" style="right:99px;top:963px">€ 100,000</div>
<div class="range-value" style="left:404px;top:965px">€ 2555</div>
<svg class="step-btn" style="left:99px;top:992px" viewBox="0 0 28 28"><circle cx="14" cy="14" r="13" fill="none" stroke="#555"/><path d="M9 14h10M14 9v10" stroke="#555"/></svg>
<div class="track" style="top:1002px"><div class="track-fill" style="width:270px"></div></div>
<div class="handle" style="left:406px;top:984px"><svg width="20" height="12" viewBox="0 0 20 12"><path d="M7 1L2 6l5 5M13 1l5 5-5 5" fill="none" stroke="var(--brand)" stroke-width="1.6"/></svg></div>
<svg class="step-btn" style="left:1073px;top:992px" viewBox="0 0 28 28"><circle cx="14" cy="14" r="13" fill="none" stroke="#555"/><path d="M9 14h10" stroke="#555"/></svg>

<div class="sum" style="left:417px">£ 181</div>
<div class="sum-op" style="left:500px">+</div>
<div class="sum" style="left:571px">£ 28.96</div>
<div class="sum-op" style="left:670px">=</div>
<div class="sum" style="left:730px">£ 209.96</div>

<div class="rep-title" style="left:99px">REPRESENTATIVE EXAMPLE</div>
<div class="rep-title" style="left:678px">CLEAR CALL</div>
<div class="rep-line" style="top:1218px"><b>AMOUNT OF CREDIT:</b> £100 FOR 13 DAYS. INTEREST RATE:292%PA (FIXED).</div>
<div class="rep-line" style="top:1244px"><b>ONE TOTAL REPAYMENT OF:</b> £110.40. REPRESENTATIVE:1,509%APR.</div>
<div class="email-field">Type Your Email</div>
<div class="btn-start">GET STARTED</div>

<section class="about" role="img" aria-label="Dim photo of a businessman with faint finance icons overlaid">
  <h2 class="about-title">WHAT IS BRIGHT HARBOUR?</h2>
  <p class="about-copy">Lending on Bright Harbour is a great way to get better returns on your money, and you'll feel good knowing that you're helping small local businesses to get the economy back up and running!</p>
  <div class="btn-read">READ MORE</div>
</section>

<h2 class="section-title" style="top:1840px">OUR MARKET PLACE</h2>
<div class="title-rule" style="top:1888px"></div>

<article class="loan-card" style="left:99px">
  <div class="loan-photo" role="img" aria-label="Two colleagues looking at a laptop in a bright office" style="background:linear-gradient(135deg,#e9ecef,#b9bec4)"></div>
  <h3 class="loan-title">LOREM IPSUM DOLOR SIT AMET</h3>
  <p class="loan-text">Ut enim ad minim veniam, quis nostrud exercitation ullamco laboris nisi ut aliquip ex ea commodo consequat enim ad minim veniam, quis nostrud exercitation ullamco laboris nisi ut aliquip ex ea commodo consequat</p>
  <div class="loan-amount">$ 961,211 <span>USD</span></div>
  <div class="loan-bar"><i style="width:94%"></i></div>
  <div class="loan-pct">98%</div><div class="loan-days">44days left</div>
</article>

<article class="loan-card" style="left:439px">
  <div class="loan-photo" role="img" aria-label="Team meeting around a white table with laptops and papers" style="background:linear-gradient(135deg,#dfe3e8,#7b8896)"></div>
  <h3 class="loan-title">LOREM IPSUM DOLOR SIT AMET</h3>
  <p class="loan-text">Ut enim ad minim veniam, quis nostrud exercitation ullamco laboris nisi ut aliquip ex ea commodo consequat enim ad minim veniam, quis nostrud exercitation ullamco laboris nisi ut aliquip ex ea commodo consequat</p>
  <div class="loan-amount">$ 655,211 <span>USD</span></div>
  <div class="loan-bar"><i style="width:62%"></i></div>
  <div class="loan-pct">58%</div><div class="loan-days">24days left</div>
</article>

<article class="loan-card" style="left:779px">
  <div class="loan-photo" role="img" aria-label="Hand pressing a glowing Solution button on a blue screen" style="background:linear-gradient(135deg,#2a5fb8,#0b1f4d)"></div>
  <h3 class="loan-title">LOREM IPSUM DOLOR SIT AMET</h3>
  <p class="loan-text">Ut enim ad minim veniam, quis nostrud exercitation ullamco laboris nisi ut aliquip ex ea commodo consequat enim ad minim veniam, quis nostrud exercitation ullamco laboris nisi ut aliquip ex ea commodo consequat</p>
  <div class="loan-amount">$ 771,211 <span>USD</span></div>
  <div class="loan-bar"><i style="width:38%"></i></div>
  <div class="loan-pct">38%</div><div class="loan-days">76days left</div>
</article>

<footer class="site-footer">
  <div class="foot-sep" style="left:293px"></div>
  <div class="foot-sep" style="left:561px"></div>
  <div class="foot-sep" style="left:792px"></div>
  <div class="foot-col" style="left:99px"><h4>FINANCE</h4><ul><li>Press Releases</li><li>Events</li><li>Downloads</li><li>Investor Realtion</li></ul></div>
  <div class="foot-col" style="left:348px"><h4>COUNTRIES</h4><ul><li>United States</li><li>Australia</li><li>France</li><li>Germany</li></ul></div>
  <div class="foot-col" style="left:620px"><h4>BRIGHT HARBOUR</h4><ul><li>Press Releases</li><li>Become a Dealer</li><li>Login to Dealer Portal</li><li>Support</li></ul></div>
  <div class="foot-col" style="left:841px"><h4>CONTACTS</h4>
    <div class="contact-row"><svg width="12" height="15" viewBox="0 0 12 15"><path d="M6 0a6 6 0 0 0-6 6c0 4 6 9 6 9s6-5 6-9a6 6 0 0 0-6-6z" fill="#fff"/><circle cx="6" cy="6" r="2" fill="var(--brand)"/></svg><span>Unit 12, Quay Street, Northgate.<br>P. O BOX 4410, Harbourton.</span></div>
    <div class="contact-row"><svg width="12" height="12" viewBox="0 0 12 12"><path d="M2 0h3l1 3-2 1a7 7 0 0 0 4 4l1-2 3 1v3c0 1-1 2-2 2A10 10 0 0 1 0 2c0-1 1-2 2-2z" fill="#fff"/></svg><span>+353 1 555 0192</span></div>
    <div class="contact-row"><svg width="12" height="10" viewBox="0 0 12 10"><rect width="12" height="10" fill="#fff"/><path d="M0 0l6 5 6-5" fill="none" stroke="var(--brand)"/></svg><span>hello@brightharbour.ie</span></div>
    <div class="social"><i></i><i></i><i></i><i></i><i></i><i></i><i></i></div>
  </div>
</footer>
<div class="legal">All Rights Reserved. ©Copyrights Bright Harbour @ 2015</div>

</body>
</html>
```